Following list to be designed:

1. A4 Letter Head

Must comprise of:
BRISK HARBOR and its LOGO
Address: No.41, 2F, Telvin Court, Marlow Lane, Upper Fennel Gardens, Bangalore 560 078
Tel: 080 41927380
Fax: 080 41927381
Mail: hello@briskharbor.example

Color of wordings to be in the lighter shade of blue and brighter shade of blue.

2. A4 Envelope

Must comprise of:
BRISK HARBOR and its LOGO
Tel: 080 41927380
Fax: 080 41927381

3. Postal Envelope

Must comprise of:
BRISK HARBOR and its LOGO
Tel: 080 41927380
Fax: 080 41927381

4. Business Card

Must comprise of:
Ravi Menon
Managing Partner
Cell: +91 9847162053
Mail: ravimenon@briskharbor.example
Tel: 080 41927380
Fax: 080 41927381

5. A4 Letter Head

Must comprise of:
BRISK HARBOR CORP. (wording) and BRISK HARBOR LOGO (only blue ribbon)

Blue ribbon (BRISK HARBOR LOGO) may be placed on Left Top Corner of the A4 Letter Head
and BRISK HARBOR CORP. (wording) to be placed on Right Top Corner of the A4 Letter Head

Tel: 080 41927380
Fax: 080 41927381

6. . A4 Envelope

Must comprise of:

Blue ribbon (BRISK HARBOR LOGO) may be placed on Left Top Corner of the A4 Envelope
and BRISK HARBOR CORP. (wording) to be placed on Right Top Corner of the A4 Envelope
Tel: 080 41927380
Fax: 080 41927381

Target Market(s)

Top IT/ITES Organizations

Industry/Entity Type

Real Estate Development

Font styles to use
Serif
Sans Serif

Colors
33a6d7
0792cd
85cae6

Requirements
Should not have
• Playful font and color

```html
<!DOCTYPE html>
<html lang="en">
<head>
<meta charset="utf-8">
<title>Brisk Harbor Stationery</title>
<link href="https://fonts.googleapis.com/css2?family=Open+Sans:wght@400;700;800&display=swap" rel="stylesheet">
<style>
  :root{
    --bg:#c9cacd;
    --paper:#ffffff;
    --blue-deep:#1a94cf;
    --blue:#33a6d7;
    --blue-light:#85cae6;
    --blue-pale:#d6eaf6;
    --ink:#5a5b5e;
  }
  *{margin:0;padding:0;box-sizing:border-box}
  html,body{width:1200px;height:1000px;overflow:hidden}
  body{background:var(--bg);font-family:"Open Sans",sans-serif;position:relative}
  .sheet{position:absolute;background:var(--paper);overflow:hidden}
  .brand-name{font-family:"Open Sans",sans-serif;font-weight:800;color:var(--ink);letter-spacing:.02em;white-space:nowrap;position:absolute}
  .brand-square{position:absolute;background:var(--blue)}
  .watermark{position:absolute;inset:0;background:linear-gradient(135deg,rgba(133,202,230,.35),rgba(133,202,230,.08) 60%,rgba(133,202,230,.3))}
  .watermark.on-blue{background:linear-gradient(135deg,rgba(133,202,230,.35),rgba(133,202,230,.1) 55%,rgba(133,202,230,.4))}
  .edge-tabs{position:absolute;left:0;width:9px}
  .edge-tabs i{display:block;height:7px}
  .edge-tabs i:nth-child(1){background:var(--blue-deep)}
  .edge-tabs i:nth-child(2){background:var(--blue)}
  .edge-tabs i:nth-child(3){background:var(--blue-light)}
  .footer-line{position:absolute;left:0;right:0;text-align:center;font-size:4.6px;font-weight:700;line-height:6px}
  .footer-line .label{color:var(--blue)}
  .footer-line .value{color:var(--blue-deep)}
  .on-blue-text{color:#fff}

  .letterhead{width:251px;height:355px;top:123px}
  .letterhead.classic{left:49px}
  .letterhead.corner{left:898px}
  .letterhead .footer-line{bottom:6px}

  .a4-envelope{width:251px;height:355px;top:517px;background:var(--blue-deep)}
  .a4-envelope .header{position:absolute;left:0;right:0;top:0;height:39px;background:var(--paper)}
  .a4-envelope .footer-line{bottom:10px}
  .a4-envelope.back .flap{position:absolute;left:0;right:0;top:0;height:40px;background:var(--paper);border-radius:0 0 12px 12px / 0 0 22px 22px;margin:0 3px}

  .card{width:106px;height:65px;top:212px}
  .card .panel{position:absolute;inset:0;background:var(--blue-deep);clip-path:polygon(16% 100%,62% 0,100% 0,100% 100%)}
  .card-details{position:absolute;left:56px;top:12px;color:#fff;font-size:3.4px;line-height:4.6px}
  .card-details .person{font-size:5.2px;font-weight:800;letter-spacing:.04em;line-height:6px}
  .card-details .role{font-size:3.3px;margin-bottom:4px}

  .dl-envelope{width:262px;height:131px;top:303px}
  .dl-envelope .panel{position:absolute;inset:0;background:var(--blue-deep);clip-path:polygon(41% 100%,83% 0,100% 0,100% 100%)}
  .dl-envelope .flap{position:absolute;left:0;right:0;top:0;height:33px;background:var(--blue-deep);border-radius:0 0 40% 40% / 0 0 25% 25%}
  .address-block{position:absolute;left:9px;top:89px;font-size:4.2px;line-height:5.6px;color:var(--ink);font-weight:700}
  .address-block span{display:inline-block;width:18px}
</style>
</head>
<body>

<!-- Letterhead: centred name -->
<section class="sheet letterhead classic">
  <div class="watermark" role="img" aria-label="Faint brand ribbon watermark"></div>
  <div class="edge-tabs" style="top:17px"><i></i><i></i><i></i></div>
  <span class="brand-name" style="left:0;right:0;text-align:center;top:24px;font-size:7px">BRISK HARBOR</span>
  <p class="footer-line" style="bottom:12px"><span class="label">Address: </span><span class="value">No.41, 2F, Telvin Court, Marlow Lane, Upper Fennel Gardens, Bangalore 560 078</span></p>
  <p class="footer-line"><span class="label">Tel: </span><span class="value">080 41927380</span> | <span class="label">Fax: </span><span class="value">080 41927381</span> | <span class="label">Mail: </span><span class="value">hello@briskharbor.example</span></p>
</section>

<!-- Business card front -->
<section class="sheet card" style="left:484px">
  <span class="brand-name" style="left:0;right:0;text-align:center;top:28px;font-size:6px">BRISK HARBOR</span>
</section>

<!-- Business card back -->
<section class="sheet card" style="left:606px">
  <div class="panel"></div>
  <span class="brand-square" style="left:14px;top:7px;width:5px;height:5px"></span>
  <span class="brand-name" style="left:21px;top:6px;font-size:4.4px">BRISK HARBOR</span>
  <div class="card-details">
    <p class="person">RAVI MENON</p>
    <p class="role">MANAGING PARTNER</p>
    <p>Cell: +91 9847162053</p>
    <p>Mail: ravimenon@briskharbor.example</p>
    <p>Tel: 080 41927380</p>
    <p>Fax: 080 41927381</p>
  </div>
</section>

<!-- DL envelope front -->
<section class="sheet dl-envelope" style="left:329px">
  <div class="panel"><div class="watermark on-blue" role="img" aria-label="Faint brand ribbon watermark"></div></div>
  <span class="brand-name" style="left:9px;top:27px;font-size:7px">BRISK HARBOR</span>
  <div class="address-block">
    <p><span>Address</span>: No.41, 2F, Telvin Court,</p>
    <p><span></span>&nbsp; Marlow Lane, Upper Fennel Gardens,</p>
    <p><span></span>&nbsp; Bangalore 560 078</p>
    <p><span>Tel</span>: 080 41927380</p>
    <p><span>Fax</span>: 080 41927381</p>
    <p><span>Mail</span>: hello@briskharbor.example</p>
  </div>
</section>

<!-- DL envelope back -->
<section class="sheet dl-envelope" style="left:606px">
  <div class="flap"></div>
  <div class="edge-tabs" style="left:auto;right:0;top:94px"><i></i><i></i><i></i></div>
</section>

<!-- Letterhead: mark left, wording right -->
<section class="sheet letterhead corner">
  <div class="watermark" role="img" aria-label="Faint brand ribbon watermark"></div>
  <div class="edge-tabs" style="top:17px"><i></i><i></i><i></i></div>
  <span class="brand-square" style="left:15px;top:11px;width:21px;height:21px"></span>
  <span class="brand-name" style="right:10px;top:16px;font-size:8px">BRISK HARBOR CORP.</span>
  <p class="footer-line" style="bottom:12px"><span class="label">Address: </span><span class="value">No.41, 2F, Telvin Court, Marlow Lane, Upper Fennel Gardens, Bangalore 560 078</span></p>
  <p class="footer-line"><span class="label">Tel: </span><span class="value">080 41927380</span> | <span class="label">Fax: </span><span class="value">080 41927381</span> | <span class="label">Mail: </span><span class="value">hello@briskharbor.example</span></p>
</section>

<!-- A4 envelope front: centred name -->
<section class="sheet a4-envelope" style="left:49px">
  <div class="watermark on-blue" role="img" aria-label="Faint brand ribbon watermark" style="top:39px"></div>
  <div class="header">
    <span class="brand-name" style="left:0;right:0;text-align:center;top:14px;font-size:7px">BRISK HARBOR</span>
  </div>
  <p class="footer-line on-blue-text" style="bottom:16px">Address: No.41, 2F, Telvin Court, Marlow Lane, Upper Fennel Gardens, Bangalore 560 078</p>
  <p class="footer-line on-blue-text">Tel: 080 41927380 | Fax: 080 41927381 | Mail: hello@briskharbor.example</p>
</section>

<!-- A4 envelope back -->
<section class="sheet a4-envelope back" style="left:313px">
  <div class="flap"></div>
</section>

<!-- A4 envelope front: mark left, wording right -->
<section class="sheet a4-envelope" style="left:636px">
  <div class="watermark on-blue" role="img" aria-label="Faint brand ribbon watermark" style="top:39px"></div>
  <div class="header">
    <span class="brand-square" style="left:11px;top:8px;width:23px;height:23px"></span>
    <span class="brand-name" style="right:11px;top:14px;font-size:8px">BRISK HARBOR CORP.</span>
  </div>
  <p class="footer-line on-blue-text" style="bottom:16px">Address: No.41, 2F, Telvin Court, Marlow Lane, Upper Fennel Gardens, Bangalore 560 078</p>
  <p class="footer-line on-blue-text">Tel: 080 41927380 | Fax: 080 41927381 | Mail: hello@briskharbor.example</p>
</section>

<!-- A4 envelope back -->
<section class="sheet a4-envelope back" style="left:898px">
  <div class="flap"></div>
</section>

</body>
</html>
```